Car Soap Label Design specifically targeting RVs

I am private labeling a car wash soap to specifically target the RV industry. It will be sold in a one gallon jug with a 6"x11" spot to place the label on front and wrap around the two sides. (see attached pics for example of label size) The front of the label I want to have a realistic picture of a high dollar class A RV somehow integrated into the design, and the key features of the soap. I had wordsmithbot design a couple that I kind of like the look of that I will attach, but open to other options. I want something clean and professional looking that will back the premium product I am selling.
The name of my brand is "Blue Harbor Gleam". I want the brand name to be somewhere on the label, but not a main focus. I want the focus to be the product and its benefits. "Premium RV Wash and Wax" as the main verbiage. Benefits... "Developed for Use With Foam Gun or Bucket with Water", "Safe for All RV Exteriors", "Protective Wax Formula", "Enhanced Shine", "Water Repellent", "Streak Free Rinse", "UV Protection". On the side...Directions: 2 Ways of Mixing... Pour Concentrate into Foam Gun Bottle OR Mixing Ratio: 1 Part Wash & Wax / 3 Parts Water in bucket. Apply soap to one side of RV at a time and use carwash brush to easily loosen road film and rinse clean. On the other side... Keep from freezing, Keep Out of Reach of Children. MADE IN USA. Hazardous Ingredients: NONE . NOTICE: The seller and/or manufacturer assumes no responsibility for damage or injury resulting from misuse of this product. No warranties, expressed or implied, are given for the performance or safety of this product.

Target Market(s)

RV industry

Industry/Entity Type

RV/Auto

Requirements
Must have
• Clean, Professional look, size 6" tall and 11" wide
Nice to have
• Realistic Class A RV as part of design

```html
<!DOCTYPE html>
<html lang="en">
<head>
<meta charset="utf-8">
<title>Premium RV Wash and Wax – Label</title>
<link href="https://fonts.googleapis.com/css2?family=Open+Sans:wght@400;700;800&display=swap" rel="stylesheet">
<style>
  :root {
    --page: #ffffff;
    --red: #c41e30;
    --red-mid: #a81a2a;
    --red-dark: #7c1320;
    --night: #1a0508;
    --white: #ffffff;
  }
  * { box-sizing: border-box; margin: 0; padding: 0; }
  html, body {
    width: 1200px; height: 1200px; overflow: hidden;
    background: var(--page);
    font-family: "Open Sans", Arial, sans-serif;
  }
  .label {
    position: absolute; left: 92px; top: 324px;
    width: 1016px; height: 552px;
    background: var(--red);
    overflow: hidden;
    color: var(--white);
    box-shadow: 6px 8px 14px rgba(0,0,0,0.35);
  }
  .label__shapes { position: absolute; inset: 0; }
  .label__photo {
    position: absolute; left: 420px; top: 0; width: 596px; height: 552px;
    background:
      radial-gradient(ellipse at 70% 55%, rgba(30,6,10,0.95) 0%, rgba(60,10,18,0.85) 40%, rgba(120,20,32,0.3) 75%, rgba(196,30,48,0) 100%),
      linear-gradient(90deg, rgba(196,30,48,0) 0%, rgba(80,12,22,0.7) 45%, var(--night) 100%);
  }
  .side-title {
    position: absolute; font-weight: 700; font-size: 14px; letter-spacing: 0.3px;
  }
  .benefits__title { left: 34px; top: 58px; }
  .benefits__list {
    position: absolute; left: 34px; top: 100px; width: 240px;
    list-style: none; font-size: 12.5px; line-height: 16px;
  }
  .benefits__list li { margin-bottom: 7px; padding-left: 12px; text-indent: -12px; }
  .benefits__list li::before { content: "> "; }
  .directions__title { left: 34px; top: 358px; }
  .directions__text {
    position: absolute; left: 34px; top: 387px; width: 276px;
    font-size: 12.5px; line-height: 16.5px;
  }
  .brand-name {
    position: absolute; left: 307px; top: 106px; width: 400px;
    text-align: center;
    font-weight: 700; font-size: 27px; color: var(--white);
  }
  .product-title {
    position: absolute; left: 320px; top: 292px; width: 380px;
    font-family: "Open Sans", Arial, sans-serif;
    font-weight: 800; color: var(--white);
    text-align: center; line-height: 1;
  }
  .product-title__main { display: block; font-size: 50px; letter-spacing: 2px; }
  .product-title__sub { display: block; font-size: 26px; margin-top: 6px; letter-spacing: 0.5px; }
  .warnings {
    position: absolute; left: 702px; top: 60px; width: 290px;
    font-weight: 700; font-size: 11.5px; line-height: 23px;
  }
  .notice {
    position: absolute; left: 702px; top: 150px; width: 290px;
    font-size: 12px; line-height: 15.5px;
  }
</style>
</head>
<body>
  <div class="label">
    <svg class="label__shapes" width="1016" height="552" viewBox="0 0 1016 552">
      <polygon points="0,0 240,0 0,240" fill="#b21b2c"/>
      <polygon points="140,0 380,0 90,552 0,552 0,330" fill="#d02537" opacity="0.55"/>
      <polygon points="380,0 560,0 230,552 60,552" fill="#b01a2b" opacity="0.6"/>
      <polygon points="300,552 520,230 700,552" fill="#a0182a" opacity="0.5"/>
      <polygon points="560,0 760,0 620,180" fill="#9a1727" opacity="0.5"/>
    </svg>
    <div class="label__photo" role="img" aria-label="Photograph of a glossy dark vehicle front with headlight, wet from washing, in red tones"></div>

    <h2 class="side-title benefits__title">BENEFITS</h2>
    <ul class="benefits__list">
      <li>Developed for Use With Foam Gun or Bucket with Water</li>
      <li>Safe for All RV Exteriors</li>
      <li>Protective Wax Formula</li>
      <li>Enhanced Shine</li>
      <li>Water Repellent</li>
      <li>Streak Free Rinse</li>
      <li>UV Protection</li>
    </ul>

    <h2 class="side-title directions__title">DIRECTIONS:</h2>
    <p class="directions__text">2 Ways of Mixing... Pour Concentrate into Foam Gun Bottle OR Mixing Ratio: 1 Part Wash &amp; Wax / 3 Parts Water in bucket. Apply soap to one side of RV at a time and use carwash brush to easily loosen road film and rinse clean.</p>

    <div class="brand-name">Blue Harbor Gleam</div>

    <h1 class="product-title">
      <span class="product-title__main">PREMIUM</span>
      <span class="product-title__sub">RV WASH AND WAX</span>
    </h1>

    <div class="warnings">
      <p>KEEP FROM FREEZING</p>
      <p>KEEP OUT OF REACH OF CHILDREN</p>
      <p>MADE IN USA</p>
    </div>
    <p class="notice">NOTICE: The seller and/or manufacturer assumes no responsibility for damage or injury resulting from misuse of this product. No warranties, expressed or implied, are given for the performance or safety of this product.</p>
  </div>
</body>
</html>
```